Webbanner-Design für Slideshow
Zielgruppe
Annegret bietet 3 Kurse an:
diese Kurse verhelfen einem selbst seine Schutzengel wieder zu hören,
mit ihnen ihren Seelenplan weshalb man auf Erden ist zu sehen,
sowie professionell umzusetzen.
Zielgruppe:
Spirituelle Menschen,
welche Engel lieben,
an sich mental gerne in Kursen & Privat arbeiten,
neues Wissen sich liebend gerne aneignen,
ihren Seelenplan wissen und umsetzen möchten,
die Schönheit im Inneren (Seele) und
im Aussen (Körper & Umgebung) lieben.
Aufgabenstellung
Produktbannerbild für meine Website (Slideshow):
Hintergrund: vorhanden in Form von einem Jpeg, hier auf diesem Foto bitte dich einfach mit folgendem beschäftigen:
Schriftzug groß: Engel (wieder) hören lernen & deinen Seelenplan umsetzen
mit Annegret Holzmeier (klein, oder großer Schriftzug?)
Schriftzug klein: mehr …
Schriftfarbe: weiss
Schriftart: moderne Schrift (z.Bsp. was die Zeitschriften benützen)
Haus Button Schriftzug: KURSE IN MUC
Buttons Ideen, Vierecke oder Kreise ect.: Transparent bitte und in passender Farbe
Stil: Modern, klar, schön, nicht verschnörkelt, unesoterisch, unverspielt
Mein Logo mit Flügel: irgendwo miteinbauen
Sonstiges: anbei noch ein Iconzeichen für Kurse Seminar
Auflösung Farbe: Text & Icons für Druck (Flyer) & Webproduktpräsentation (Slideshow)
Maße: (bei 1600xca.872 px., bleiben, Banner nicht verkleinern, oder ranzoomen)

```html
<!DOCTYPE html>
<html lang="de">
<head>
<meta charset="utf-8">
<title>Engel wieder hören lernen – Kursbanner</title>
<link rel="stylesheet" href="https://fonts.googleapis.com/css2?family=Raleway:wght@300;400&family=Pathway+Gothic+One&family=Antonio:wght@100&display=swap">
<style>
  :root {
    --text-white: #ffffff;
    --badge-rose: rgba(232, 128, 132, 0.78);
    --room-light: #f1e6e3;
    --room-mid: #e2d0cb;
    --room-warm: #d9bfb4;
    --floor: #b89a88;
    --shadow: rgba(40, 25, 20, 0.55);
  }
  * { margin: 0; padding: 0; box-sizing: border-box; }
  html, body { width: 1200px; height: 644px; overflow: hidden; background: #fff; }
  .banner {
    position: relative;
    width: 1200px;
    height: 644px;
    overflow: hidden;
    font-family: "Raleway", sans-serif;
    color: var(--text-white);
  }
  .banner__photo {
    position: absolute;
    inset: 0;
    background:
      radial-gradient(ellipse at 55% 35%, #f8efec 0%, rgba(248,239,236,0) 60%),
      linear-gradient(180deg, var(--room-light) 0%, var(--room-mid) 55%, var(--room-warm) 82%, var(--floor) 100%);
  }
  .brand {
    position: absolute;
    left: 22px;
    top: 40px;
    display: flex;
    align-items: center;
    gap: 8px;
    font-family: "Pathway Gothic One", sans-serif;
    font-size: 30px;
    letter-spacing: 1px;
  }
  .brand__dot {
    width: 14px; height: 14px;
    border-radius: 50%;
    background: var(--text-white);
  }
  .badge {
    position: absolute;
    left: 909px;
    top: 30px;
    width: 222px;
    height: 222px;
    border-radius: 50%;
    background: var(--badge-rose);
  }
  .badge__icon {
    position: absolute;
    left: 66px;
    top: 31px;
    width: 90px;
    height: 90px;
  }
  .badge__label {
    position: absolute;
    left: 50%;
    top: 122px;
    white-space: nowrap;
    font-family: "Pathway Gothic One", sans-serif;
    font-size: 62px;
    line-height: 1;
    transform: translateX(-50%) scaleX(0.58);
    text-shadow: 1px 2px 3px var(--shadow);
  }
  .headline {
    font-weight: normal;
    text-shadow: 1px 2px 4px var(--shadow);
  }
  .headline > span {
    position: absolute;
    white-space: nowrap;
    line-height: 1;
    transform-origin: left top;
  }
  .headline__main {
    left: 205px;
    top: 395px;
    font-family: "Raleway", sans-serif;
    font-weight: 400;
    font-size: 88px;
    letter-spacing: 1px;
  }
  .headline__tail {
    left: 499px;
    top: 433px;
    font-family: "Pathway Gothic One", sans-serif;
    font-size: 46px;
    transform: scaleX(0.76);
  }
  .headline__second {
    left: 208px;
    top: 474px;
    font-family: "Pathway Gothic One", sans-serif;
    font-size: 50px;
    letter-spacing: 1px;
  }
  .headline__second .cap { font-size: 62px; }
  .presenter {
    position: absolute;
    left: 300px;
    top: 538px;
    white-space: nowrap;
    font-family: "Antonio", sans-serif;
    font-weight: 100;
    font-size: 66px;
    letter-spacing: 2px;
    line-height: 1;
    transform-origin: left top;
    transform: scaleX(0.74);
    text-shadow: 1px 2px 4px var(--shadow);
  }
</style>
</head>
<body>
  <main class="banner">
    <div class="banner__photo" role="img" aria-label="Foto: Kursleiterin am weißen Schreibtisch in hellem, rosé eingerichtetem Raum mit Blumen und Schminktisch"></div>

    <div class="brand"><span class="brand__dot"></span>Lichtflug</div>

    <div class="badge">
      <svg class="badge__icon" viewBox="0 0 90 90" aria-hidden="true">
        <circle cx="45" cy="45" r="42" fill="none" stroke="#fff" stroke-width="4"/>
        <path d="M45 22 L68 44 L62 44 L62 64 L28 64 L28 44 L22 44 Z" fill="#fff"/>
        <rect x="56" y="26" width="5" height="11" fill="#fff"/>
        <rect x="40" y="50" width="10" height="14" fill="var(--badge-rose)"/>
      </svg>
      <div class="badge__label">KURSE IN MUC</div>
    </div>

    <h1 class="headline">
      <span class="headline__main">ENGEL</span>
      <span class="headline__tail">WIEDER HÖREN LERNEN &amp;</span>
      <span class="headline__second">EINEN&nbsp;&nbsp;<span class="cap">S</span>EELENPLAN&nbsp;&nbsp;UMSETZEN</span>
    </h1>

    <p class="presenter">Mit Annegret Holzmeier</p>
  </main>
</body>
</html>
```